Gin bottle designs - micro distillery

We are an Italian Distillery in Melbourne Australia. We would like to modernise the brand and in particular the bottle labels. We need to get a lable that will look better on the shelf while still maintaining the Italian "feel" of the product.

You can also refer to web site: www.trevinaspirits.com for a background.

At this time we are stuck with the rectangular bottles. We can consider different configurations (like a top label and a wrap around label at the bottom

The key message is more modern and attention grabbing.

Target Market(s)

Alcohol drinkers

Requirements
Must have
• GIN
Mediterranean Gin
Grappa
Brandy
Vodka

```html
<!DOCTYPE html>
<html lang="en">
<head>
<meta charset="utf-8">
<title>Trevina Gin Labels</title>
<link href="https://fonts.googleapis.com/css2?family=Cinzel:wght@600;700&family=Bebas+Neue&family=Montserrat:wght@800&family=Roboto+Condensed:wght@400&family=Allura&display=swap" rel="stylesheet">
<style>
  :root {
    --page: #ffffff;
    --label: #fbfbf8;
    --label-edge: #e4e4df;
    --ink: #2b2b2b;
    --gold: #c9a648;
    --gold-deep: #a8842f;
    --red: #c23a30;
    --signature: #e0584a;
    --badge: #2c2a27;
    --it-green: #2e9a47;
    --it-white: #ffffff;
    --it-red: #d8362f;
    --scene-light: #d9d9d6;
    --scene-dark: #2a2a2a;
  }
  * { margin: 0; padding: 0; box-sizing: border-box; }
  html, body { width: 873px; height: 1200px; overflow: hidden; background: var(--page); }
  .canvas { position: relative; width: 873px; height: 1200px; }
  .label {
    position: absolute;
    top: 233px;
    width: 224px;
    height: 877px;
    background: var(--label);
    border: 1px solid var(--label-edge);
  }
  .label--mediterranean { left: 139px; }
  .label--grappa { left: 520px; }
  .label > * { position: absolute; left: 0; right: 0; text-align: center; }
  .brand {
    top: 62px;
    display: flex;
    flex-direction: column;
    align-items: center;
    gap: 12px;
  }
  .brand-name {
    font-family: "Cinzel", serif;
    font-weight: 700;
    font-size: 25px;
    line-height: 1;
    letter-spacing: 2px;
    color: var(--ink);
  }
  .brand-dot { width: 14px; height: 14px; border-radius: 50%; background: var(--ink); }
  .landscape {
    top: 201px;
    left: 11px;
    right: auto;
    width: 201px;
    height: 465px;
    border-radius: 0 0 100px 100px;
    background: linear-gradient(180deg, var(--scene-light) 0%, #bdbdba 35%, #5a5a58 55%, var(--scene-dark) 80%, #4a4a48 100%);
  }
  .label--grappa .landscape { top: 214px; }
  .variant {
    top: 677px;
    font-family: "Bebas Neue", sans-serif;
    font-size: 25px;
    line-height: 1;
    letter-spacing: 7px;
    padding-left: 7px;
  }
  .variant--mediterranean { color: var(--gold); }
  .variant--grappa { top: 686px; color: var(--red); font-size: 30px; letter-spacing: 9px; padding-left: 9px; }
  .spirit {
    top: 700px;
    font-family: "Montserrat", sans-serif;
    font-weight: 800;
    font-size: 37px;
    line-height: 1;
    letter-spacing: 6px;
    padding-left: 6px;
    color: var(--ink);
  }
  .label--grappa .spirit { top: 713px; }
  .heritage {
    top: 745px;
    left: 6px;
    right: 6px;
    height: 58px;
    background: var(--badge);
    padding: 4px;
  }
  .label--grappa .heritage { top: 751px; }
  .heritage-frame {
    width: 100%;
    height: 100%;
    border: 1px solid var(--gold-deep);
    display: flex;
    flex-direction: column;
    align-items: center;
    justify-content: center;
  }
  .heritage-title {
    font-family: "Cinzel", serif;
    font-weight: 700;
    font-size: 15px;
    line-height: 1.05;
    letter-spacing: 1px;
    color: var(--gold);
  }
  .heritage-sub {
    font-family: "Cinzel", serif;
    font-weight: 600;
    font-size: 10px;
    line-height: 1.1;
    letter-spacing: 1px;
    color: var(--gold-deep);
  }
  .tricolour { display: flex; gap: 2px; margin-top: 2px; }
  .tricolour span { width: 9px; height: 9px; border-radius: 50%; }
  .tricolour .green { background: var(--it-green); }
  .tricolour .white { background: var(--it-white); }
  .tricolour .red { background: var(--it-red); }
  .signature {
    top: 811px;
    font-family: "Allura", cursive;
    font-size: 28px;
    line-height: 1;
    color: var(--signature);
  }
  .label--grappa .signature { top: 816px; }
  .details {
    top: auto;
    left: 10px;
    right: 10px;
    bottom: 14px;
    display: flex;
    justify-content: space-between;
    font-family: "Roboto Condensed", sans-serif;
    font-size: 13px;
    line-height: 1;
    color: var(--ink);
  }
</style>
</head>
<body>
<main class="canvas">
  <article class="label label--mediterranean">
    <header class="brand">
      <span class="brand-name">TREVINA</span>
      <span class="brand-dot"></span>
    </header>
    <div class="landscape" role="img" aria-label="Engraved black and white vineyard landscape with rows of vines under a cloudy sky"></div>
    <p class="variant variant--mediterranean">MEDITERRANEAN</p>
    <h1 class="spirit">GIN</h1>
    <div class="heritage">
      <div class="heritage-frame">
        <span class="heritage-title">ITALIAN HERITAGE</span>
        <span class="heritage-sub">AUSSIE SPIRIT</span>
        <div class="tricolour"><span class="red"></span><span class="white"></span><span class="green"></span></div>
      </div>
    </div>
    <p class="signature">Leo Marchetti</p>
    <footer class="details"><span>300mL</span><span>25% ALC/VOL</span></footer>
  </article>

  <article class="label label--grappa">
    <header class="brand">
      <span class="brand-name">TREVINA</span>
      <span class="brand-dot"></span>
    </header>
    <div class="landscape" role="img" aria-label="Engraved black and white vineyard landscape with rows of vines under a cloudy sky"></div>
    <p class="variant variant--grappa">GRAPPA</p>
    <h1 class="spirit">GIN</h1>
    <div class="heritage">
      <div class="heritage-frame">
        <span class="heritage-title">ITALIAN HERITAGE</span>
        <span class="heritage-sub">AUSSIE SPIRIT</span>
        <div class="tricolour"><span class="red"></span><span class="white"></span><span class="green"></span></div>
      </div>
    </div>
    <p class="signature">Leo Marchetti</p>
    <footer class="details"><span>300mL</span><span>25% ALC/VOL</span></footer>
  </article>
</main>
</body>
</html>
```